Bauzaunbanner für Fertigung und Montagen von Metallbau- und Stahlkonstruktionen
Zielgruppe
Fertigung und Montagen von Metallbau- und Stahlkonstruktionen
Aufgabenstellung
Außenwerbung an unserem Produktionsstandort (große halle); Blickdistanz ca. 50m; Stellengesuch 'Monteure' (w/m/d); Breite ca. 5.000mm; einfache (Bild-)Botschaft

```html
<!DOCTYPE html>
<html lang="de">
<head>
<meta charset="utf-8">
<title>Monteure gesucht – Bauzaunbanner</title>
<link rel="stylesheet" href="https://fonts.googleapis.com/css2?family=Noto+Sans:wght@600;700;800&display=swap">
<style>
  :root {
    --page: #ffffff;
    --banner-dark: #25282e;
    --banner-mid: #3a3f47;
    --sky-light: #8c93a0;
    --sky-dark: #323a4a;
    --yellow: #f6c30b;
    --white: #f4f4f4;
    --grey-text: #d6d6d6;
    --ink: #1c1c1c;
    --rule: rgba(220, 220, 220, 0.55);
  }
  * { margin: 0; padding: 0; box-sizing: border-box; }
  html, body {
    width: 1200px; height: 675px; overflow: hidden;
    background: var(--page);
    font-family: "Noto Sans", Arial, sans-serif;
  }
  .banner {
    position: absolute; left: 146px; top: 147px;
    width: 952px; height: 424px; overflow: hidden;
    background: radial-gradient(ellipse at 75% 45%, var(--banner-mid), var(--banner-dark) 75%);
  }
  .hero-photo {
    position: absolute; left: 0; top: 0; width: 560px; height: 424px;
    background: linear-gradient(180deg, var(--sky-dark) 0%, var(--sky-light) 38%, #4a505c 62%, #2b2f36 100%);
    -webkit-mask-image: linear-gradient(90deg, #000 65%, transparent 100%);
    mask-image: linear-gradient(90deg, #000 65%, transparent 100%);
  }
  .rule {
    position: absolute; right: 0; height: 2px;
    background: linear-gradient(90deg, transparent, var(--rule) 25%, var(--rule));
  }
  .rule--top { left: 354px; top: 62px; }
  .rule--bottom { left: 350px; top: 315px; }
  .line {
    position: absolute; left: 388px; width: 560px;
    text-align: center; white-space: nowrap; line-height: 1;
  }
  .kicker { top: 19px; font-size: 32px; font-weight: 700; color: var(--white); letter-spacing: 0.5px; }
  .headline { color: var(--yellow); font-weight: 800; text-shadow: 0 3px 6px rgba(0,0,0,0.6); }
  .headline--job { top: 65px; font-size: 78px; letter-spacing: -2px; }
  .headline--gender { top: 143px; font-size: 35px; font-weight: 700; }
  .headline--sought { top: 175px; font-size: 64px; letter-spacing: -1px; }
  .trade { top: 257px; font-size: 27px; font-weight: 600; color: var(--white); }
  .web-pill {
    position: absolute; left: 522px; top: 307px; width: 305px; height: 47px;
    border-radius: 11px; background: var(--yellow);
    display: flex; align-items: center; justify-content: center;
    font-size: 29px; font-weight: 700; color: var(--ink); white-space: nowrap; line-height: 1;
  }
  .slogan {
    position: absolute; left: 244px; top: 366px; line-height: 1;
    font-size: 24.5px; font-weight: 700; color: var(--grey-text); white-space: nowrap;
  }
</style>
</head>
<body>
  <section class="banner">
    <div class="hero-photo" role="img" aria-label="Foto einer modernen Industriehalle mit Glasfassade und Rolltoren unter dramatisch bewölktem Himmel"></div>
    <div class="rule rule--top"></div>
    <div class="rule rule--bottom"></div>
    <p class="line kicker">JETZT BEWERBEN</p>
    <h1 class="line headline headline--job">MONTEURE</h1>
    <p class="line headline headline--gender">(m/w/d)</p>
    <p class="line headline headline--sought">GESUCHT!</p>
    <p class="line trade">Metallbau &amp; Stahlkonstruktionen</p>
    <div class="web-pill">www.brenning.de</div>
    <p class="slogan">BAU MIT UNS DIE ZUKUNFT AUS STAHL</p>
  </section>
</body>
</html>
```